Business Card Design

Consultation for design, construction athletic facilities specializing in synthetic turf systems and all weather running track systems.
Motto "True Owner Representation"
New Company that we'd like to highlight the LOGO first and foremost with the colors of the background and font as primary colors of the card too if possible. I've also attached a typical larger project design layout that could be used in the background to highlight our design and construction specialty.
Website is something we want very noticeable for driving traffic.
Target Market(s)
Athletic Directors, Designers, Government and Military, Contractors
Industry/Entity Type
Construction
Contact Information for Business Card
Peter L. Vandrell CFB, CTB
48317 W 63rd Ave
Harlow Ridge, WA 99482
C +1 503.555.0147
O +1 808.555.0182
Peter@fieldlaneco.example
www.fieldlaneco.example

```html
<!DOCTYPE html>
<html lang="en">
<head>
<meta charset="utf-8">
<title>Corvana Sport — Business Card</title>
<link rel="stylesheet" href="https://fonts.googleapis.com/css2?family=Exo+2:wght@400;500&family=Tinos:wght@400;700&display=swap">
<style>
  :root {
    --page: #ffffff;
    --card-black: #050505;
    --card-edge: #d9d9d9;
    --gold-dark: #5a3a10;
    --gold-bright: #f3c35a;
    --copper: #d9892e;
    --name-orange: #e39a3c;
    --credential: #cfc6b6;
    --ink: #111111;
    --drawing-light: #f7f7f7;
    --drawing-mid: #e6e6e6;
    --contact-light: #e6dcc8;
  }
  * { box-sizing: border-box; margin: 0; padding: 0; }
  html, body {
    width: 1200px; height: 1000px; overflow: hidden;
    background: var(--page);
  }
  .canvas { position: relative; width: 1200px; height: 1000px; }

  .card {
    position: absolute; top: 127px;
    width: 500px; height: 284px;
    overflow: hidden;
  }
  .card--front { left: 73px; background: var(--card-black); }
  .card--back { left: 638px; background: var(--page); border: 1px solid var(--card-edge); }

  .gold-rule {
    position: absolute; left: 0; right: 0; top: 202px; height: 5px;
    background: linear-gradient(90deg, var(--gold-dark) 0%, #8a5e1e 30%, var(--gold-bright) 55%, #8a5e1e 80%, var(--gold-dark) 100%);
  }
  .lower-band {
    position: absolute; left: 0; right: 0; top: 207px; bottom: 0;
    background: var(--card-black);
  }

  /* front */
  .brand-dot {
    position: absolute; left: 60px; top: 38px;
    width: 110px; height: 110px; border-radius: 50%;
    background: #1a1108;
  }
  .brand-name {
    position: absolute; left: 185px; top: 70px;
    font-family: "Exo 2", sans-serif; font-weight: 400;
    font-size: 38px; letter-spacing: 3px;
    color: var(--copper);
  }
  .holder {
    position: absolute; left: 0; right: 0; top: 214px;
    text-align: center;
  }
  .holder__name {
    font-family: "Exo 2", sans-serif; font-weight: 500;
    font-size: 20px; letter-spacing: 1px;
    color: var(--name-orange); line-height: 1.2;
  }
  .holder__credential {
    font-family: "Tinos", serif; font-size: 20px;
    color: var(--credential); line-height: 1.3;
  }

  /* back */
  .site-plan {
    position: absolute; left: 0; top: 0; right: 0; height: 202px;
    background: radial-gradient(ellipse at 45% 50%, var(--drawing-mid) 0%, var(--drawing-light) 60%, #ffffff 100%);
  }
  .contact-block {
    position: absolute; left: 0; right: 0; top: 50px;
    text-align: center;
    font-family: "Tinos", serif; font-weight: 700;
    font-size: 20px; color: var(--ink); line-height: 29px;
  }
  .contact-block .gap { margin-top: 8px; }
  .online {
    position: absolute; left: 0; right: 0; top: 217px;
    text-align: center;
    font-family: "Tinos", serif; font-size: 20px;
    color: var(--contact-light); line-height: 26px;
  }
</style>
</head>
<body>
<main class="canvas">
  <section class="card card--front" aria-label="Card front">
    <div class="brand-dot"></div>
    <div class="brand-name">Corvana Sport</div>
    <div class="gold-rule"></div>
    <div class="lower-band"></div>
    <div class="holder">
      <p class="holder__name">Peter L. Vandrell</p>
      <p class="holder__credential">CFB</p>
    </div>
  </section>

  <section class="card card--back" aria-label="Card back">
    <div class="site-plan" role="img" aria-label="Faint technical site plan of an athletic track and field layout"></div>
    <div class="contact-block">
      <p>Ph:+1 503.555.0147 O</p>
      <p>+1 808.555.0182</p>
      <p class="gap">CTB 48317 W 63rd</p>
      <p>Ave Harlow Ridge, WA 99482 C</p>
    </div>
    <div class="gold-rule"></div>
    <div class="lower-band"></div>
    <div class="online">
      <p>E: peter@fieldlaneco.example</p>
      <p>W: www.fieldlaneco.example</p>
    </div>
  </section>
</main>
</body>
</html>
```